Need Web Design for Business Process Outsourcing Company (Korvenza)

Korvenza is a business process outsourcing company. Need a simple site similar to http://www.taskmeridianhub.com/ but with a more professional and credible look. New to the process; not sure where to start and comparing my options. Please let me know what my options are if I choose to go with you. Logo is attached for your reference. Please use same colorway

Reason: I want the final product to be coded. Please confirm you will be able to code final design.

Industry/Entity Type

Business

Coding

Coded - Design and coding required

```html
<!DOCTYPE html>
<html lang="en">
<head>
<meta charset="utf-8">
<title>Korvenza Services</title>
<link rel="stylesheet" href="https://fonts.googleapis.com/css2?family=Arimo:wght@400;700&display=swap">
<style>
  :root{
    --navy:#2c3068;
    --blue:#1a5e8e;
    --button:#1273b5;
    --ink:#222222;
    --muted:#555555;
    --band-light:#ebebeb;
    --band-dark:#adadad;
    --red:#dc4a38;
    --fb:#34559a;
    --green:#2e9a5c;
    --orange:#f39a1f;
  }
  *{margin:0;padding:0;box-sizing:border-box}
  html,body{width:960px;height:1200px;overflow:hidden;background:#fff}
  body{position:relative;font-family:"Arimo",Arial,sans-serif;color:var(--ink)}
  .page{position:absolute;left:133px;top:0;width:681px;height:1200px}
  .abs{position:absolute}
  .center{left:0;width:681px;text-align:center}

  .hero{left:0;top:0;width:681px;height:354px;overflow:hidden}
  .hero-photo{position:absolute;inset:0;background:linear-gradient(110deg,#e9f0f4 0%,#dbe6ec 45%,#c9d6de 70%,#b7c7d1 100%)}
  .menu{position:absolute;right:5px;top:4px;width:22px;height:18px;border:1px solid var(--button);background:#fff;padding:3px}
  .menu span{display:block;height:2px;background:var(--button);margin-bottom:2px}
  .brand{position:absolute;top:38px;left:0;width:681px;display:flex;justify-content:center;align-items:center;gap:12px}
  .brand-mark{width:52px;height:52px;background:var(--button)}
  .brand-name{font-size:48px;font-weight:700;color:#3d3d3f;letter-spacing:-1px}
  .hero-title{top:121px;font-size:26px;color:var(--navy);letter-spacing:.3px}
  .hero-text{top:163px;left:150px;width:381px;text-align:center;font-size:15px;line-height:20.5px;color:#333}
  .cta{left:261px;top:241px;width:162px;height:29px;background:linear-gradient(#1a86c9,#0f5f99);color:#fff;font-size:20px;line-height:29px;text-align:center}

  .section-title{font-size:22px;color:var(--blue)}
  .services-title{top:373px}
  .service{width:108px;text-align:center}
  .service h3{font-size:10px;font-weight:400;color:var(--ink)}
  .service p{font-size:7.5px;line-height:13px;color:var(--muted);margin-top:8px}
  .dots{display:flex;gap:6px}
  .dot{width:10px;height:10px;border-radius:50%;background:#777}
  .dot.active{background:var(--blue)}

  .trust-title{top:617px;font-size:23px;color:var(--ink)}
  .feature{width:120px;text-align:center}
  .feature h4{font-size:7.5px;font-weight:400;letter-spacing:.3px;color:var(--ink)}
  .feature p{font-size:5.6px;line-height:8px;color:#333;margin-top:8px}

  .reviews-title{top:822px;font-size:22px;color:var(--ink)}
  .reviews{left:0;top:859px;width:681px;height:164px;background:var(--band-light)}
  .review{width:180px;text-align:center}
  .avatar{width:50px;height:50px;border-radius:50%;margin:0 auto;background:radial-gradient(circle at 50% 40%,#e7c9a8,#8aa3c0);border:1px solid #999}
  .review h5{font-size:8.5px;font-weight:400;margin-top:10px}
  .review p{font-size:6.5px;line-height:9px;margin-top:10px}
  .reviews .dot{background:#aaa;border:1px solid #888}
  .reviews .dot.active{background:var(--navy)}

  .join{left:0;top:1023px;width:681px;height:118px;background:var(--band-dark);color:#fff;text-align:center}
  .join h2{font-size:14px;font-weight:400;margin-top:13px}
  .join p{font-size:7.6px;line-height:11.3px;width:390px;margin:16px auto 0}
  .social{position:absolute;top:97px;height:16px;width:103px;color:#fff;font-size:6.5px;line-height:16px;display:flex;align-items:center;justify-content:center;gap:8px}
  .social i{display:block;width:8px;height:8px;background:rgba(255,255,255,.85)}
  .social.pluma{left:236px;background:var(--red)}
  .social.circlet{left:347px;background:var(--fb)}

  .footer-nav{top:1156px;display:flex;justify-content:center;gap:19px;font-size:6.5px;color:#555;letter-spacing:.2px}
  .footer-icons{top:1172px;display:flex;justify-content:center;gap:4px}
  .footer-icons span{width:6px;height:6px;border-radius:50%;background:#999}
  .footer-legal{top:1188px;display:flex;justify-content:center;gap:13px;font-size:6.3px;color:#555}
</style>
</head>
<body>
<div class="page">

  <header class="hero abs">
    <div class="hero-photo" role="img" aria-label="Photo of a modern glass office tower seen from below"></div>
    <div class="menu"><span></span><span></span><span></span></div>
    <div class="brand"><div class="brand-mark"></div><div class="brand-name">Korvenza</div></div>
    <h1 class="hero-title abs center" style="font-weight:400">MAXIMIZE PERFORMANCE</h1>
    <p class="hero-text abs">Lorem Ipsum is simply dummy text of the printing and typesetting industry. Lorem Ipsum has been the industry's standard dummy</p>
    <div class="cta abs">Get Move</div>
  </header>

  <h2 class="section-title services-title abs center" style="font-weight:400">OUTSOURCING SERVICES</h2>
  <svg class="abs" style="left:0;top:410px" width="681" height="130" viewBox="0 0 681 130">
    <circle cx="195" cy="63" r="54" fill="none" stroke="#7b6f96" stroke-width="0.8"/>
    <path d="M297 22 A54 54 0 0 1 385 22 M297 104 A54 54 0 0 0 385 104" fill="none" stroke="#666" stroke-width="0.8"/>
    <path d="M440 22 A54 54 0 0 1 528 22 M440 104 A54 54 0 0 0 528 104" fill="none" stroke="#666" stroke-width="0.8"/>
    <rect x="191" y="31" width="7" height="10" fill="none" stroke="#666" stroke-width="0.8"/>
    <circle cx="199" cy="42" r="2" fill="#666"/>
    <circle cx="341" cy="37" r="7" fill="none" stroke="#666" stroke-width="0.7"/>
    <text x="341" y="40" font-size="8" text-anchor="middle" fill="#666" font-family="Arimo, sans-serif">?</text>
    <circle cx="484" cy="36" r="3.5" fill="none" stroke="#777" stroke-width="0.7"/>
    <line x1="482.5" y1="41" x2="485.5" y2="41" stroke="#777" stroke-width="0.7"/>
  </svg>
  <div class="service abs" style="left:141px;top:466px"><h3>Customer Service</h3><p>Customer advocacy is the core of our support.</p></div>
  <div class="service abs" style="left:287px;top:466px"><h3>Ecommerce</h3><p>Given our own experi-ence,</p></div>
  <div class="service abs" style="left:430px;top:466px"><h3>Creative</h3><p>With a talented pool of personnel,</p></div>
  <div class="dots abs" style="left:314px;top:546px"><span class="dot active"></span><span class="dot"></span><span class="dot"></span><span class="dot"></span></div>

  <h2 class="trust-title abs center" style="font-weight:400">Trust &amp; Safety</h2>
  <svg class="abs" style="left:173px;top:658px" width="42" height="48" viewBox="0 0 42 48">
    <path d="M21 2 L39 8 V22 C39 34 31 42 21 46 C11 42 3 34 3 22 V8 Z" fill="var(--green)"/>
    <path d="M12 24 L19 31 L31 16" fill="none" stroke="#fff" stroke-width="5" stroke-linecap="round" stroke-linejoin="round"/>
  </svg>
  <svg class="abs" style="left:322px;top:660px" width="46" height="46" viewBox="0 0 46 46">
    <path d="M3 5 H24 M3 5 V42 H24 L32 34 V28" fill="none" stroke="var(--orange)" stroke-width="3.5"/>
    <path d="M22 42 L32 32 L22 32 Z" fill="var(--orange)"/>
    <circle cx="26" cy="14" r="9" fill="#bfe0f2" stroke="var(--navy)" stroke-width="3"/>
    <line x1="32" y1="21" x2="41" y2="30" stroke="var(--navy)" stroke-width="4" stroke-linecap="round"/>
  </svg>
  <div class="abs" style="left:462px;top:664px;width:48px;height:38px;background:linear-gradient(160deg,#a6d65a,#5c9a2a)" role="img" aria-label="Illustration of the word success rising as a green arrow"></div>
  <div class="feature abs" style="left:133px;top:716px"><h4>REINVENTING SERVICES</h4><p>Lorem Ipsum is simply dummy text of the printing and typesetting industry. Lorem Ipsum has been the industry's standard dummy text ever since the 1500s</p></div>
  <div class="feature abs" style="left:278px;top:716px"><h4>OUR FACILITIES</h4><p>Lorem Ipsum is simply dummy text of the printing and typesetting industry. Lorem Ipsum has been the industry's standard dummy text ever since the 1500s</p></div>
  <div class="feature abs" style="left:424px;top:716px"><h4>SUCCESS STORIES</h4><p>Lorem Ipsum is simply dummy text of the printing and typesetting industry. Lorem Ipsum has been the industry's standard dummy text ever since the 1500s</p></div>

  <h2 class="reviews-title abs center" style="font-weight:400">Customer Reviews</h2>
  <section class="reviews abs">
    <div class="review abs" style="left:150px;top:22px">
      <div class="avatar" role="img" aria-label="Portrait photo of a smiling couple"></div>
      <h5>Patricia K. Sofa</h5>
      <p>Great Service! Right on time, got the job done fast, would definitely recommend!</p>
    </div>
    <div class="review abs" style="left:355px;top:22px">
      <div class="avatar" role="img" aria-label="Photo of a happy couple sitting outdoors"></div>
      <h5>Patricia K. Sofa</h5>
      <p>Great Service! Right on time, got the job done fast, would definitely recommend!</p>
    </div>
    <div class="dots abs" style="left:316px;top:148px"><span class="dot active"></span><span class="dot"></span><span class="dot"></span><span class="dot"></span></div>
  </section>

  <section class="join abs">
    <h2>Passionate about engaging with clients and growing business?</h2>
    <p>Meridian Staffing is composed of equally talented pool of professionals coming from diverse backgrounds and culture. We value individuality and contribute fully and pro-actively to achieve our clients' goals. If you are passionate with interacting with people and resolving their issues, or if you are a problem solver and love challenges, you might be the one we need!</p>
    <div class="social pluma"><i></i>Sign in with Pluma</div>
    <div class="social circlet"><i></i>Connect with Circlet</div>
  </section>

  <nav class="footer-nav abs center">
    <span>WHO WE ARE</span><span>OUR SOLUTIONS</span><span>OUR STRATEGY</span><span>OUR EXPERIENCE</span><span>SECURITY</span><span>NEWS</span><span>CONTACT US</span>
  </nav>
  <div class="footer-icons abs center"><span></span><span></span></div>
  <div class="footer-legal abs center"><span>©2016 ABC</span><span>TERMS PRIVACY</span><span>PARTNER WITH US</span><span>CAREERS</span></div>

</div>
</body>
</html>
```